http://www.brightmeadowfold.org/

would like someone to rebuild this -http://www.brightmeadowfold.com/ to be more modern and more easily updated

Industry/Entity Type

Non Profit

Coding

Coded - Design and coding required

Colors

Designer to choose colors to be used in the design.

Requirements
Must have
• use of the logo, and a newer design for wordpress to be hosted on Azure and easily updated templates

```html
<!DOCTYPE html>
<html lang="en">
<head>
<meta charset="utf-8">
<title>Bright Meadow Fold</title>
<link rel="stylesheet" href="https://fonts.googleapis.com/css2?family=Roboto+Slab:wght@300;400;500;700&display=swap">
<style>
:root{
  --ink:#231c3a;
  --ink-soft:#3a3350;
  --text:#333;
  --muted:#555;
  --paper:#fff;
  --mist:#f2f7fb;
  --band:#2d375c;
  --line:#e2e2e6;
}
*{box-sizing:border-box;margin:0;padding:0}
html,body{width:1200px;height:3472px;overflow:hidden}
body{position:relative;background:var(--paper);font-family:"Roboto Slab",serif;color:var(--text)}
.abs{position:absolute}
a{color:inherit;text-decoration:none}

/* header */
.site-header{position:absolute;left:0;top:0;width:1200px;height:131px;background:var(--paper);z-index:3}
.brand-badge{position:absolute;left:166px;top:16px;width:150px;height:150px;border-radius:50%;background:var(--paper);box-shadow:0 3px 8px rgba(0,0,0,.15);display:flex;align-items:center;justify-content:center;text-align:center;z-index:4}
.brand-badge span{font-size:17px;font-weight:700;color:var(--ink);line-height:1.2;width:110px}
.tel{position:absolute;left:590px;top:24px;font-size:19px;font-weight:500;color:var(--ink);display:flex;align-items:center;gap:8px}
.btn-letter{position:absolute;left:815px;top:20px;width:212px;height:35px;border-radius:18px;background:var(--ink);color:#fff;font-size:12.5px;font-weight:500;display:flex;align-items:center;justify-content:center;letter-spacing:.2px}
.nav{position:absolute;left:346px;top:84px;display:flex;gap:27px;font-size:13px;color:var(--text)}
.nav .active{position:relative;padding:0 7px}
.nav .active::before,.nav .active::after{content:"";position:absolute;top:-2px;width:4px;height:20px;border:1px solid var(--ink);border-radius:50%}
.nav .active::before{left:-2px;border-right:none}
.nav .active::after{right:-2px;border-left:none}

/* hero */
.hero{position:absolute;left:0;top:131px;width:1200px;height:675px;background:radial-gradient(ellipse at 50% 55%,#6b5341 0%,#4a3a30 40%,#2f3240 75%,#5c5a58 100%)}
.hero-box{position:absolute;left:295px;top:189px;width:610px;height:240px;background:rgba(20,18,22,.72);text-align:center;color:#fff}
.hero-box h1{font-size:42px;font-weight:700;margin-top:46px;letter-spacing:.5px}
.hero-box p{font-size:26px;font-style:italic;font-weight:300;margin-top:6px}
.hero-box .btn-donate{display:inline-block;margin-top:16px;width:162px;height:44px;line-height:40px;border:2px solid #fff;border-radius:24px;background:var(--ink);font-size:16px;font-weight:500}

/* feature card */
.features{position:absolute;left:171px;top:748px;width:856px;height:314px;background:var(--paper);box-shadow:0 2px 10px rgba(0,0,0,.14);display:flex;padding-top:37px;z-index:2}
.feature{flex:1;text-align:center}
.feature .ring{width:84px;height:84px;margin:0 auto;border:2px solid var(--ink);border-radius:50%;display:flex;align-items:center;justify-content:center}
.feature h3{font-size:15px;font-weight:500;color:var(--ink);margin-top:18px}
.feature p{font-size:11.5px;line-height:22px;color:var(--muted);margin:10px auto 0;width:210px}

/* about */
.about{position:absolute;left:0;top:1120px;width:1200px;height:656px;background:var(--mist)}
.about-photo{position:absolute;left:172px;top:134px;width:434px;height:382px;background:linear-gradient(135deg,#3a2a30 0%,#a04a2a 35%,#5d8ba0 55%,#7a2f2a 80%,#2a1d1d 100%)}
.about-card{position:absolute;left:516px;top:109px;width:511px;height:430px;background:var(--paper);box-shadow:0 2px 10px rgba(0,0,0,.14);padding:72px 52px 0 129px}
.about-card h2{font-size:30px;font-weight:500;color:var(--ink)}
.about-card p{font-size:11px;line-height:22.5px;color:var(--text);margin-top:18px;text-align:justify}
.btn-dark{display:inline-block;margin-top:25px;width:110px;height:36px;line-height:36px;text-align:center;border-radius:18px;background:var(--ink);color:#fff;font-size:12px;font-weight:500}

/* banner */
.letter-band{position:absolute;left:0;top:1776px;width:1200px;height:217px;background:linear-gradient(180deg,#2a3052 0%,#2f3a60 60%,#35426a 100%);text-align:right;padding:82px 173px 0 0}
.letter-band a{display:block;color:#fff;font-size:25px;line-height:34px;text-decoration:underline;text-underline-offset:4px}

/* media */
.media-title{position:absolute;left:0;top:2104px;width:1200px;text-align:center;font-size:30px;font-weight:500;color:var(--ink)}
.media-card{position:absolute;background:var(--paper);box-shadow:0 2px 10px rgba(0,0,0,.12);text-align:center}
.media-card .thumb{position:absolute;left:50%;top:-71px;margin-left:-91px;width:182px;height:182px;border-radius:50%;border:3px solid var(--ink);padding:5px;background:var(--paper)}
.media-card .thumb div{width:100%;height:100%;border-radius:50%}
.media-card h3{font-size:16px;font-weight:500;color:var(--ink);margin-top:139px}
.media-card p{font-size:12.5px;line-height:22.5px;color:var(--muted);margin:15px auto 0;width:240px}

/* history */
.portrait{position:absolute;left:123px;top:2680px;width:424px;height:424px;border-radius:50%;border:4px solid var(--ink);padding:26px;background:var(--paper)}
.portrait div{width:100%;height:100%;border-radius:50%;background:radial-gradient(circle at 50% 40%,#c49a82 0%,#7a5a4a 45%,#1a1416 85%)}
.history{position:absolute;left:645px;top:2738px;width:360px}
.history h2{font-size:30px;font-weight:500;color:var(--ink)}
.history h3{font-size:20px;font-weight:500;color:var(--ink-soft);margin-top:8px}
.history p{font-size:11px;line-height:22.5px;color:var(--text);margin-top:20px;text-align:justify}

/* footer */
.footer{position:absolute;left:0;top:3110px;width:1200px;height:362px}
.foot-logo{position:absolute;left:175px;top:140px;width:186px;height:186px;border-radius:50%;border:3px solid #fff;display:flex;align-items:center;justify-content:center;text-align:center}
.foot-logo span{color:#fff;font-size:20px;font-weight:700;line-height:1.25;width:130px}
.contact{position:absolute;display:flex;align-items:center;gap:22px;color:#fff;font-size:13px;font-weight:500;line-height:22px}
.contact .dot{width:56px;height:56px;border-radius:50%;background:#fff;display:flex;align-items:center;justify-content:center;flex:none}
.foot-rule{position:absolute;left:435px;top:250px;width:592px;height:1px;background:rgba(255,255,255,.25)}
.copy{position:absolute;left:436px;top:302px;color:#fff;font-size:12px}
.social{position:absolute;left:862px;top:297px;display:flex;gap:26px}
.social span{width:22px;height:22px;border-radius:50%;border:2px solid #fff}
</style>
</head>
<body>

<header class="site-header">
  <div class="brand-badge"><span>Bright Meadow Fold</span></div>
  <div class="tel">
    <svg width="18" height="18" viewBox="0 0 24 24"><path fill="#231c3a" d="M6.6 10.8a15.1 15.1 0 0 0 6.6 6.6l2.2-2.2a1 1 0 0 1 1-.25 11.4 11.4 0 0 0 3.6.57 1 1 0 0 1 1 1V20a1 1 0 0 1-1 1A17 17 0 0 1 3 4a1 1 0 0 1 1-1h3.5a1 1 0 0 1 1 1c0 1.25.2 2.46.57 3.6a1 1 0 0 1-.25 1z"/></svg>
    TEL:1 (555) 014-2260
  </div>
  <a class="btn-letter" href="#">DOWNLOAD LATEST LETTER</a>
  <nav class="nav">
    <a class="active" href="#">Home</a>
    <a href="#">About Us</a>
    <a href="#">Projects</a>
    <a href="#">Newsletters &amp; Reports</a>
    <a href="#">Media</a>
    <a href="#">What's New</a>
    <a href="#">Donation</a>
    <a href="#">Contact Us</a>
  </nav>
</header>

<section class="hero" role="img" aria-label="Photo of people holding hands in prayer around a wooden table">
  <svg class="abs" style="left:36px;top:274px" width="34" height="62" viewBox="0 0 34 62"><path d="M32 2 3 31l29 29" fill="none" stroke="#fff" stroke-width="2.5"/></svg>
  <svg class="abs" style="left:1128px;top:274px" width="34" height="62" viewBox="0 0 34 62"><path d="m2 2 29 29L2 60" fill="none" stroke="#fff" stroke-width="2.5"/></svg>
  <div class="hero-box">
    <h1>BRIGHT MEADOW FOLD</h1>
    <p>Helping the needy Christian families</p>
    <a class="btn-donate" href="#">DONATE NOW</a>
  </div>
</section>

<section class="features">
  <div class="feature">
    <div class="ring"><svg width="36" height="40" viewBox="0 0 36 40" fill="none" stroke="#231c3a" stroke-width="2.2" stroke-linecap="round"><path d="M10 18V8a2.5 2.5 0 0 1 5 0v8M15 16V5a2.5 2.5 0 0 1 5 0v11M20 16V6a2.5 2.5 0 0 1 5 0v12M25 18v-8a2.5 2.5 0 0 1 5 0v12c0 8-5 14-12 14-5 0-8-3-11-8l-3-6a2.5 2.5 0 0 1 4-2.5L10 22"/></svg></div>
    <h3>WHAT'S NEW</h3>
    <p>Sed ut perspiciatis unde omnis iste natus error sit voluptatem accusanum dolor emque laudantium, totam rem aperi amq ue ipsa quaeentor</p>
  </div>
  <div class="feature">
    <div class="ring"><svg width="38" height="34" viewBox="0 0 38 34"><path d="M19 31 5 17A8.5 8.5 0 0 1 19 6a8.5 8.5 0 0 1 14 11z" fill="none" stroke="#231c3a" stroke-width="2.4" stroke-linejoin="round"/></svg></div>
    <h3>DONATION NOW</h3>
    <p>Sed ut perspiciatis unde omnis iste natus error sit voluptatem accusanum dolor emque laudantium, totam rem aperi amq ue ipsa quaeentor</p>
  </div>
  <div class="feature">
    <div class="ring"><svg width="38" height="36" viewBox="0 0 38 36" fill="none" stroke="#231c3a" stroke-width="2.2" stroke-linejoin="round"><path d="M3 14 19 3l16 11v19H3z"/><path d="M8 18V7h22v11"/><path d="M3 14l16 11 16-11M3 33l12-10M35 33 23 23"/><path d="M12 11h14M12 15h14"/></svg></div>
    <h3>NEWSLETTERS</h3>
    <p>Sed ut perspiciatis unde omnis iste natus error sit voluptatem accusanum dolor emque laudantium, totam rem aperi amq ue ipsa quaeentor</p>
  </div>
</section>

<section class="about">
  <div class="about-photo" role="img" aria-label="Painting of a warmly lit church interior with a stained glass window"></div>
  <div class="about-card">
    <h2>ABOUT US</h2>
    <p>Then the King will say to those on His right hand, ‘Come, you blessed of My Father, inherit the kingdom prepared for you from the foundation of the world: for I was hungry and you gave Me food; I was thirsty and you gave Me drink; I was a stranger and you took Me in; I was naked and you clothed Me; I was sick and you visited Me; I was in prison and you came to Me.’ “Assuredly, I say to you, inasmuch as you did it to one of the least of these My brethren, you did it to Me.”</p>
    <a class="btn-dark" href="#">READ MORE</a>
  </div>
</section>

<section class="letter-band" role="img" aria-label="Dusk city skyline behind a dark blue overlay">
  <a href="#">Click here to read or</a>
  <a href="#">Download our latest letter for April, 2019</a>
</section>

<h2 class="media-title">MEDIA</h2>
<article class="media-card" style="left:171px;top:2254px;width:285px;height:318px">
  <div class="thumb"><div role="img" aria-label="Photo of women in colourful robes walking with children" style="background:linear-gradient(135deg,#9aa07a,#6a8a4a 40%,#b05a8a 70%,#7a6a5a)"></div></div>
  <h3>FINIBUS BONORUM</h3>
  <p>Sed ut perspiciatis unde omnis iste natus error sit voluptatem accusanium doloremque laudantium, totam rem ap quia consequuntur magni dolor</p>
</article>
<article class="media-card" style="left:745px;top:2254px;width:282px;height:318px">
  <div class="thumb"><div role="img" aria-label="Photo of a religious leader in ornate vestments" style="background:radial-gradient(circle at 50% 40%,#b08a5a,#6a3a2a 60%,#2a1a16)"></div></div>
  <h3>FINIBUS BONORUM</h3>
  <p>Sed ut perspiciatis unde omnis iste natus error sit voluptatem accusanium doloremque laudantium, totam rem ap quia consequuntur magni dolor</p>
</article>
<article class="media-card" style="left:453px;top:2238px;width:293px;height:349px;z-index:1">
  <div class="thumb"><div role="img" aria-label="Photo of a young child resting on a wooden fence" style="background:linear-gradient(160deg,#6a8a5a,#8a9a6a 40%,#5a3a2a 70%,#3a2a20)"></div></div>
  <h3>FINIBUS BONORUM</h3>
  <p>Sed ut perspiciatis unde omnis iste natus error sit voluptatem accusanium doloremque laudantium, totam rem ap quia consequuntur magni dolor</p>
</article>

<svg class="abs" style="left:60px;top:2872px" width="22" height="40" viewBox="0 0 22 40"><path d="M20 2 3 20l17 18" fill="none" stroke="#777" stroke-width="3"/></svg>
<svg class="abs" style="left:585px;top:2876px" width="22" height="40" viewBox="0 0 22 40"><path d="m2 2 17 18L2 38" fill="none" stroke="#777" stroke-width="3"/></svg>
<div class="portrait"><div role="img" aria-label="Portrait photo of the founder in formal evening wear"></div></div>
<section class="history">
  <h2>HISTORY</h2>
  <h3>Dr. Samir Hanna Toubar</h3>
  <p>Samir Toubar was born in Tanta, Egypt, on August 4, 1946. He completed his medical degree, and married Laila Fahmy on June 21, 1974. In 1981, the family settled in the United States. Over the years, the family has lived in Ohio, Oregon, Texas, and Georgia. Dr. Samir quietly and generously served his local parish. He is survived by his wife, Laila Toubar, his three children, Adel, Peter, and Hana, and his daughter-in-law and grandchild, Nadia and Clara.</p>
</section>

<footer class="footer">
  <svg class="abs" style="left:0;top:0" width="1200" height="362" viewBox="0 0 1200 362">
    <path d="M0 14C140 70 300 96 520 80 760 60 980 20 1200 30V362H0z" fill="#c9c8cf"/>
    <path d="M0 70C160 104 330 112 540 94 770 72 980 40 1200 54V362H0z" fill="#221a37"/>
  </svg>
  <div class="foot-logo"><span>Bright Meadow Fold</span></div>
  <div class="contact" style="left:434px;top:152px">
    <div class="dot"><svg width="18" height="24" viewBox="0 0 18 24"><path d="M9 0a9 9 0 0 0-9 9c0 7 9 15 9 15s9-8 9-15a9 9 0 0 0-9-9zm0 12.5A3.5 3.5 0 1 1 9 5.5a3.5 3.5 0 0 1 0 7z" fill="#221a37"/></svg></div>
    <div>P.O. BOX 480512<br>LARKFIELD, VIRGINIA 20990-0512</div>
  </div>
  <div class="contact" style="left:781px;top:152px;gap:16px">
    <div class="dot"><svg width="22" height="22" viewBox="0 0 24 24"><path fill="#221a37" d="M6.6 10.8a15.1 15.1 0 0 0 6.6 6.6l2.2-2.2a1 1 0 0 1 1-.25 11.4 11.4 0 0 0 3.6.57 1 1 0 0 1 1 1V20a1 1 0 0 1-1 1A17 17 0 0 1 3 4a1 1 0 0 1 1-1h3.5a1 1 0 0 1 1 1c0 1.25.2 2.46.57 3.6a1 1 0 0 1-.25 1z"/></svg></div>
    <div>OUR NEW TELEPHONE<br>NUMBER: 1 (555) 014-2260</div>
  </div>
  <div class="foot-rule"></div>
  <div class="copy">© 2019 Bright Meadow Fold All rights reserved.</div>
  <div class="social" aria-label="Social links">
    <span></span><span></span><span></span><span></span>
  </div>
</footer>

</body>
</html>
```